Deisgn A Manual Cover for an Australian Health Training Company

We are looking for an A4 Front of Manual Cover Design for a comprehensive administrative training manual to be launched soon in Australia.

The title of the book is :

"Drafting, Shaping and Delivering Office Paperwork"

for the Australian Medical Office (smaller font)

Written and compiled by Mel Trosk

Target Market(s)

25-45 year old medical administrative students (usually female)

Industry/Entity Type

It Company

Font styles to use
Serif

Colors
3176b5
f68d4c
33b8a4
fffbf0

Requirements
Must have
• University like perhaps
• Human element (picture/s of people)
• About the concept of designing and producing documents in a health setting (this can be entirely conceptual).
• Conceptual design would be considered
• Appealing

```html
<!DOCTYPE html>
<html lang="en">
<head>
<meta charset="utf-8">
<title>Drafting, Shaping and Delivering Office Paperwork — Manual Cover</title>
<link rel="stylesheet" href="https://fonts.googleapis.com/css2?family=Oswald:wght@400;500;700&display=swap">
<style>
  :root {
    --stage: #e4e4e4;
    --cover-teal: #5ba5b4;
    --cover-teal-dark: #4a93a2;
    --accent-orange: #e8804a;
    --paper-white: #ffffff;
    --band-white: #f4f4f2;
    --author-green: #2aa490;
    --crest-navy: #1f3550;
    --text-white: #ffffff;
  }
  html, body {
    margin: 0;
    padding: 0;
    width: 1200px;
    height: 784px;
    overflow: hidden;
    background: var(--stage);
  }
  .stage {
    position: relative;
    width: 1200px;
    height: 784px;
    display: flex;
    align-items: center;
    justify-content: center;
  }
  .cover {
    position: relative;
    width: 530px;
    height: 750px;
    background: var(--cover-teal);
    box-shadow: 0 10px 30px rgba(0,0,0,0.18);
    font-family: "Oswald", "Arial Narrow", sans-serif;
    color: var(--text-white);
    overflow: hidden;
  }
  .institute-tag {
    position: absolute;
    top: 0;
    left: 50%;
    transform: translateX(-50%);
    width: 104px;
    height: 96px;
    background: var(--paper-white);
    border-top: 8px solid var(--accent-orange);
    box-sizing: border-box;
    display: flex;
    flex-direction: column;
    align-items: center;
    justify-content: center;
    gap: 6px;
  }
  .institute-tag__mark {
    width: 18px;
    height: 18px;
    background: var(--crest-navy);
  }
  .institute-tag__name {
    font-size: 9px;
    font-weight: 500;
    line-height: 1.2;
    letter-spacing: 0.06em;
    text-align: center;
    color: var(--crest-navy);
    text-transform: uppercase;
  }
  .concept-art {
    position: absolute;
    top: 112px;
    left: 95px;
    width: 340px;
    height: 120px;
    border-radius: 6px;
    background: linear-gradient(90deg, rgba(255,255,255,0.18), rgba(232,128,74,0.55) 50%, rgba(255,255,255,0.18));
  }
  .title {
    position: absolute;
    top: 240px;
    left: 0;
    right: 0;
    margin: 0;
    text-align: center;
    font-weight: 700;
    text-transform: uppercase;
    line-height: 0.92;
  }
  .title__line {
    display: block;
    font-size: 74px;
    letter-spacing: 0.01em;
  }
  .title__line--wide { font-size: 66px; }
  .title__joiner {
    display: flex;
    align-items: center;
    justify-content: center;
    gap: 8px;
    font-size: 13px;
    font-weight: 500;
    letter-spacing: 0.1em;
    margin: 4px 0 2px;
  }
  .rule {
    display: block;
    width: 130px;
    height: 2px;
    background: var(--text-white);
  }
  .title__highlight {
    display: inline-block;
    margin-top: 8px;
    padding: 4px 16px 6px;
    background: var(--accent-orange);
  }
  .title__highlight .title__line { font-size: 64px; }
  .subtitle {
    position: absolute;
    top: 590px;
    left: 0;
    right: 0;
    text-align: center;
    font-size: 15px;
    font-weight: 500;
    letter-spacing: 0.04em;
    text-transform: uppercase;
  }
  .credit-label {
    position: absolute;
    top: 626px;
    left: 0;
    right: 0;
    display: flex;
    align-items: center;
    justify-content: center;
    gap: 10px;
    font-size: 9px;
    font-weight: 500;
    letter-spacing: 0.1em;
    text-transform: uppercase;
  }
  .credit-label .rule { width: 90px; height: 1px; }
  .author-band {
    position: absolute;
    left: 0;
    right: 0;
    bottom: 0;
    height: 100px;
    background: var(--band-white);
    display: flex;
    align-items: center;
    justify-content: center;
  }
  .author-band__name {
    font-size: 44px;
    font-weight: 700;
    letter-spacing: 0.03em;
    color: var(--author-green);
    text-transform: uppercase;
  }
</style>
</head>
<body>
  <main class="stage">
    <article class="cover">
      <div class="institute-tag">
        <span class="institute-tag__mark"></span>
        <span class="institute-tag__name">Harbour Institute<br>of Training</span>
      </div>

      <div class="concept-art" role="img" aria-label="Flat illustration of a desktop monitor showing a document, surrounded by medical office icons: heart monitor, clinic, ambulance, microscope, pills and charts"></div>

      <h1 class="title">
        <span class="title__line">Drafting,</span>
        <span class="title__line">Shaping</span>
        <span class="title__joiner"><span class="rule"></span>and<span class="rule"></span></span>
        <span class="title__line title__line--wide">Delivering</span>
        <span class="title__highlight">
          <span class="title__line">Office</span>
          <span class="title__line">Paperwork</span>
        </span>
      </h1>

      <p class="subtitle">For the Australian Medical Office</p>

      <p class="credit-label"><span class="rule"></span>Written and compiled by<span class="rule"></span></p>

      <footer class="author-band">
        <span class="author-band__name">Mel Trosk</span>
      </footer>
    </article>
  </main>
</body>
</html>
```